Larchmont Holdings Needs New Stationery Design

We need new clean and white stationery for our property management company based in Winnipeg, Manitoba, Canada. We manage condominium and commercial properties. Additionally, we do real estate development and commercial leasing.

We'll require the following:
- Business cards
- Letterhead*
- Envelope (we mainly use #10, single window envelope)
- Fax Cover Sheet
- *Electronic version of the letterhead that works in Google Docs (.jpg for top header)

Industry/Entity Type

Property Management

```html
<!DOCTYPE html>
<html lang="en">
<head>
<meta charset="utf-8">
<title>Larchmont Holdings — Stationery</title>
<link rel="stylesheet" href="https://fonts.googleapis.com/css2?family=Open+Sans:wght@400;600;700&display=swap">
<style>
  :root {
    --board: #3b3b3c;
    --paper: #f5f5f6;
    --paper-grey: #e6e6e8;
    --navy: #173f6b;
    --navy-deep: #0f3862;
    --cyan: #29a8d8;
    --ink: #4a4f57;
    --window: #ffffff;
  }
  * { box-sizing: border-box; margin: 0; padding: 0; }
  html, body { width: 1168px; height: 1200px; overflow: hidden; }
  body {
    position: relative;
    background: var(--board);
    font-family: "Open Sans", Arial, sans-serif;
    color: var(--ink);
  }
  .sheet { position: absolute; box-shadow: 0 4px 14px rgba(0,0,0,.45); }

  .brand {
    display: flex; align-items: center; gap: 7px;
    color: var(--navy); font-weight: 700; letter-spacing: -0.3px; white-space: nowrap;
  }
  .brand-square { width: 10px; height: 10px; background: var(--cyan); flex: none; }

  .rule { position: absolute; height: 2px; background: var(--cyan); }

  /* Letterhead */
  .letterhead { left: 59px; top: 114px; width: 707px; height: 966px; background: var(--paper); }
  .letterhead .brand { position: absolute; left: 0; right: 0; top: 46px; justify-content: center; font-size: 27px; }
  .letterhead .rule-left { left: 0; top: 92px; width: 280px; }
  .letterhead .rule-right { left: 280px; top: 97px; width: 427px; }
  .letterhead-footer-company { position: absolute; left: 67px; top: 912px; }
  .company-name { color: var(--navy); font-size: 13px; font-weight: 600; letter-spacing: .3px; text-transform: uppercase; }
  .company-address { font-size: 7.5px; letter-spacing: .2px; text-transform: uppercase; margin-top: 3px; }
  .letterhead-footer-contact { position: absolute; right: 56px; top: 884px; text-align: right; font-size: 11px; line-height: 15px; color: var(--navy); }

  /* Envelope */
  .envelope { left: 246px; top: 574px; width: 868px; height: 390px; background: var(--paper-grey); }
  .envelope .brand { position: absolute; left: 22px; top: 30px; font-size: 26px; }
  .envelope .rule { left: 0; top: 81px; width: 868px; }
  .envelope-return { position: absolute; left: 24px; top: 91px; }
  .envelope-return .company-name { font-size: 11px; }
  .envelope-return .company-address { font-size: 6.5px; }
  .envelope-window { position: absolute; left: 390px; top: 244px; width: 397px; height: 74px; border-radius: 20px; background: var(--window); }

  /* Business cards */
  .card { left: 609px; width: 339px; height: 204px; }
  .card-front { top: 252px; background: var(--paper-grey); }
  .card-front .brand {
    position: absolute; left: 14px; top: 64px; width: 150px;
    font-size: 18px; line-height: 20px; white-space: normal;
  }
  .card-person { position: absolute; left: 190px; top: 30px; }
  .person-name { color: var(--navy); font-size: 11px; font-weight: 700; letter-spacing: .3px; text-transform: uppercase; }
  .person-title { font-size: 6.5px; text-transform: uppercase; letter-spacing: .3px; }
  .card-details { position: absolute; left: 190px; top: 80px; font-size: 8px; line-height: 11px; }
  .card-details .gap { margin-top: 8px; }
  .card-email { position: absolute; left: 190px; top: 168px; font-size: 8px; }
  .card-front .rule-left { left: 0; top: 196px; width: 72px; }
  .card-front .rule-right { left: 72px; top: 200px; width: 267px; }
  .card-back { top: 478px; background: var(--navy-deep); }
  .card-back .brand { position: absolute; left: 0; right: 0; top: 86px; justify-content: center; font-size: 24px; color: #e9eef4; }
</style>
</head>
<body>

  <section class="sheet letterhead" aria-label="Letterhead">
    <div class="brand"><span class="brand-square"></span>Larchmont Holdings</div>
    <div class="rule rule-left"></div>
    <div class="rule rule-right"></div>
    <div class="letterhead-footer-company">
      <p class="company-name">Larchmont Holdings Corp</p>
      <p class="company-address">412 Elm Street , Winnipeg, MB R3L 1K4</p>
    </div>
    <div class="letterhead-footer-contact">
      <p>T: (204) 555-0142</p>
      <p>F: (204) 555-0143</p>
      <p>info@larchmontholdings.ca</p>
      <p>www.larchmontholdings.ca</p>
    </div>
  </section>

  <section class="sheet envelope" aria-label="Window envelope">
    <div class="brand"><span class="brand-square"></span>Larchmont Holdings</div>
    <div class="rule"></div>
    <div class="envelope-return">
      <p class="company-name">Larchmont Holdings Corp</p>
      <p class="company-address">412 Elm Street , Winnipeg, MB R3L 1K4</p>
    </div>
    <div class="envelope-window"></div>
  </section>

  <section class="sheet card card-front" aria-label="Business card front">
    <div class="brand"><span class="brand-square"></span><span class="brand-name">Larchmont<br>Holdings</span></div>
    <div class="card-person">
      <p class="person-name">Martin Keller</p>
      <p class="person-title">President &amp; CEO</p>
    </div>
    <div class="card-details">
      <p>412 Elm Street</p>
      <p>Winnipeg, MB R3L 1K4</p>
      <p class="gap">T: (204) 555-0142</p>
      <p>F: (204) 555-0143</p>
      <p>info@larchmontholdings.ca</p>
      <p>www.larchmontholdings.ca</p>
    </div>
    <p class="card-email">mkeller@larchmontholdings.ca</p>
    <div class="rule rule-left"></div>
    <div class="rule rule-right"></div>
  </section>

  <section class="sheet card card-back" aria-label="Business card back">
    <div class="brand"><span class="brand-square"></span>Larchmont Holdings</div>
  </section>

</body>
</html>
```